依頼詳細
****************************
全国各地で少年詩を創作している詩人たちの応募作品の中から、「子どもにもわかる言葉で書かれた文学性の高い詩作品」を選定し発表しているアンソロジーです。
1984年から年刊「明日童謡選」として20年刊継続してまいりました。2004年より「こどもとひらく童心詩選」と改題し、新たな体制で少年詩のより一層の普及と質的向上をめざしています。

参加費:掲載された場合には予価2,400円(税別)の本を5冊以上ご購入いただきます。(割引あり)(別途送料)*別紙の規約など参照。

選定は任期3年で7名の編集委員により実施されております。
現在の編集委員は
杉浦航一郎(詩人・絵本作家)
くらもと・さよこ(詩人)
島田 薫(小説家・緑陵大学教授)
●●●●(詩人)*未確定なので、一旦この記載
●●●●(詩人)*未確定なので、一旦この記載
岡部里香子(青い窓舎 代表取締役)
森川静江(青い窓舎 編集長)

以上7名です。
編集委員により掲載・不掲載が決定しますが、各編集委員には「5点」を持ち点として、校正刷りの段階で優秀な作品に点数を振り分けてもらい、最優秀作品を決定しております。
最優秀賞に賞金などは出ませんが、粗品を贈呈しております。

なお、学校に協力してもらい、校正刷りの段階にて授業などで活用し、子どもたちの感想を直接もらう取り組みをしております。また実際に詩人を授業に招待する活動もしています。
子どもたちには「好きな作品3つ選んで」とお願いをしてコメントをもらっています。
編集委員、子どもたちの集計結果とコメントは刊行される『こどもとひらく童心詩選』に挟み込まれる「ことのは便り」にて紹介させていただいております。集まった子どもの感想は詩人たちにフィードバックしております。(毎年約400名以上の生徒が参加。)

刊行後は主に公共図書館や学校図書館に納品されます。もちろん全国の書店やBookvaleなどでも購入可能です。
*******************************

主に郵送でご案内をします。
全国各地で詩を書いている人、約2,000人にDMする予定です。
DMの一番トップに、今回のチラシを添えたいと考えております。
同封物として、規定や確認書なども同封します。
が、規約などの細かな部分は読まないので、パッと見ただけで「あ〜、子どもたちを読書対象とした作品の募集をしているんだな。」が理解できると嬉しいです。

他者にない特徴としては、上記にもある《校正刷りの段階で学校と協力して授業でも活用している》ことだと感じています。

作品応募・掲載→編集委員・生徒の感想フィードバック→次年度に質的向上した詩作品の応募・・・このサイクルを目指しています。
生徒にとってもテストの点数に関係がない「詩を味わう時間」という贅沢な時間を経験し、言葉の引き出しを増やしてもらっています。

主に郵送でご案内をします。
全国各地で物語を書いている人、約2,000人にDMする予定です。
同封物として、規定や確認書なども同封します。
が、規約などの細かな部分は読まないですし、パッと見ただけで「あ〜、子どもたちを読書対象とした作品の募集をしているんだな。」が理解できると嬉しいです。

投稿は専用の原稿用紙のみ受け付けとなっているので、弊社に問い合わせ(投稿規定や原稿用紙)をいただけるようにしていただけると幸いです。
記載項目
社名、書名、編集委員、締め切り、問い合わせ先など
サイズ
A4
ページ数
片面
希望イメージ
シンプル 複雑
単色 カラフル
暗い 明るい
日常 高級
遊び心 厳粛
未来的 伝統的
女性的 男性的
希望する色
設定なし
納品ファイル
• イラストレーター形式 (.ai)
• フォトショップ形式 (.psd)
補足説明
*今回より編集委員が変更になっております。
*チラシは昨年のワークリンク採用作品です。
■ 選んだ理由

応募内容などの文字が読みやすいこと。
締め切りの3月末の春を迎える寸前の雰囲気を感じること。
などから選ばせていただきました。

■ 提案者全員のお礼・コメント

この度も素敵なご提案をありがとうございました!
票が全て割れるような事態になるくらい、最終的には好みの段階で選考させていただくような結果となりました。
今後ともよろしくお願いします。

```html
<!DOCTYPE html>
<html lang="ja">
<head>
<meta charset="utf-8">
<title>こどもとひらく童心詩選 2019 作品募集</title>
<link rel="stylesheet" href="https://fonts.googleapis.com/css2?family=Noto+Sans+JP:wght@400;700&family=Noto+Serif+JP:wght@400;600&display=swap">
<style>
:root{
  --paper:#fbf6e6;
  --sky:#8ecbea;
  --sky-soft:#d6ecf7;
  --sky-line:#86c3e3;
  --orange:#f2a24e;
  --brown:#a3713c;
  --ink:#3a3a3a;
  --white:#ffffff;
}
*{margin:0;padding:0;box-sizing:border-box}
html,body{width:849px;height:1200px;overflow:hidden;background:var(--paper)}
.flyer{position:relative;width:849px;height:1200px;background:var(--paper);font-family:"Noto Sans JP",sans-serif;color:var(--ink)}
.hero-figure{position:absolute;left:130px;top:0;width:440px;height:650px;background:linear-gradient(180deg,#9ad2ef,#84c3e6);border-radius:0 0 200px 200px / 0 0 60px 60px}
.title-sub{position:absolute;left:400px;top:100px;writing-mode:vertical-rl;white-space:nowrap;font-family:"Noto Serif JP",serif;font-size:30px;letter-spacing:4px;line-height:1;color:var(--white)}
.title-main{position:absolute;left:318px;top:170px;writing-mode:vertical-rl;white-space:nowrap;font-family:"Noto Serif JP",serif;font-size:62px;font-weight:600;letter-spacing:10px;line-height:1;color:var(--white)}
.year{position:absolute;left:270px;top:555px;width:160px;text-align:center;font-family:"Noto Serif JP",serif;font-size:36px;letter-spacing:6px;line-height:1;color:var(--white)}
.call{position:absolute;left:720px;top:34px;width:92px;height:230px;background:var(--orange);color:var(--white);writing-mode:vertical-rl;white-space:nowrap;font-family:"Noto Serif JP",serif;font-size:44px;font-weight:600;letter-spacing:6px;line-height:1;display:flex;align-items:center;justify-content:center}
.lead{position:absolute;left:56px;top:160px;height:400px;writing-mode:vertical-rl;white-space:nowrap;font-family:"Noto Serif JP",serif;font-size:22px;line-height:40px;letter-spacing:3px;color:var(--brown)}
.info{position:absolute;left:45px;top:652px;width:760px;height:455px;background:var(--white);border:2px solid var(--sky-line);border-radius:8px;padding:18px 20px;display:grid;grid-template-columns:1fr 1fr;column-gap:26px}
.col{display:flex;flex-direction:column;gap:14px}
.section h2{background:var(--sky-soft);font-size:13px;font-weight:700;text-align:center;padding:6px 0;margin-bottom:8px;color:#2f4f66}
.section p{font-size:10.5px;line-height:1.75;margin-bottom:4px}
.section ul{list-style:none;font-size:10.5px;line-height:1.7}
.footer{position:absolute;left:45px;top:1118px;width:760px;height:70px}
.publisher{position:absolute;left:0;top:6px;display:flex;align-items:center;gap:12px}
.publisher .mark{width:14px;height:14px;border-radius:50%;background:var(--sky-line)}
.publisher .name-block{font-size:11px;line-height:1.3}
.publisher .name{font-size:18px;font-weight:700}
.publisher .addr{font-size:9.5px;line-height:1.55;margin-left:10px}
.deadline{position:absolute;right:0;top:-6px;width:190px;border:2px solid var(--orange);text-align:center}
.deadline .label{background:var(--orange);color:var(--white);font-size:13px;font-weight:700;padding:3px 0}
.deadline .date{font-size:13px;font-weight:700;color:var(--orange);padding:6px 0;background:var(--white)}
</style>
</head>
<body>
<main class="flyer">
  <div class="hero-figure" role="img" aria-label="子どもの横顔のシルエットのイラスト（水色）"></div>
  <h1>
    <span class="title-sub">こどもとひらく</span>
    <span class="title-main">童心詩選</span>
  </h1>
  <p class="year">2019</p>
  <p class="call">作品募集</p>
  <p class="lead">子どもたちのこころに響かせる<br>詩篇をお待ちしております。</p>

  <section class="info">
    <div class="col">
      <div class="section">
        <h2>こどもとひらく童心詩選について</h2>
        <p>全国各地で少年詩を創作している詩人たちの応募作品の中から、「子どもにもわかる言葉で書かれた文学性の高い詩作品」を選定し発表しているアンソロジーです。1984年から年刊「明日童謡選」として20年刊継続してまいりました。2004年より「こどもとひらく童心詩選」と改題し、新たな体制で少年詩のより一層の普及と質的向上をめざしています。</p>
        <p>校正刷りの段階で学校と協力し、授業で活用して子どもたちの感想を直接いただいています。集まった感想は「ことのは便り」にて紹介し、詩人たちにフィードバックしております。</p>
      </div>
      <div class="section">
        <h2>投稿方法について</h2>
        <p>応募作品は専用の原稿用紙のみ受け付けております。投稿規定および原稿用紙をご希望の方は、下記の弊社までお問い合わせください。</p>
        <p>規定や確認書をご確認のうえ、ご応募ください。</p>
      </div>
    </div>
    <div class="col">
      <div class="section">
        <h2>参加費について</h2>
        <p>掲載された場合には予価2,400円（税別）の本を5冊以上ご購入いただきます。（割引あり）（別途送料）＊詳しくは別紙の規約などをご参照ください。</p>
      </div>
      <div class="section">
        <h2>選考について</h2>
        <ul>
          <li>杉浦航一郎（詩人・絵本作家）</li>
          <li>くらもと・さよこ（詩人）</li>
          <li>島田 薫（小説家・緑陵大学教授）</li>
          <li>●●●●（詩人）</li>
          <li>●●●●（詩人）</li>
          <li>岡部里香子（青い窓舎 代表取締役）</li>
          <li>森川静江（青い窓舎 編集長）</li>
        </ul>
        <p>任期3年の編集委員7名により掲載・不掲載を決定します。各編集委員が持ち点「5点」を優秀な作品に振り分け、最優秀作品を決定いたします。最優秀賞には粗品を贈呈しております。</p>
      </div>
    </div>
  </section>

  <footer class="footer">
    <div class="publisher">
      <span class="mark"></span>
      <div class="name-block">株式会社<br><span class="name">青い窓舎</span></div>
      <p class="addr">〒248-0031　海浜県港町緑ヶ丘2-14-7<br>TEL 045-555-0193　FAX 045-555-0194<br>http://www.aoimado-sha.example　info@aoimado-sha.example</p>
    </div>
    <div class="deadline">
      <p class="label">応募締め切り</p>
      <p class="date">2019年3月末日弊社必着</p>
    </div>
  </footer>
</main>
</body>
</html>
```